Flyer für Fahrschule
Zielgruppe
Die Fahrschule Sonnenkamp in Rastede bietet eine moderne und umfassende Ausbildung vom Mofa bis zum Bus. Ob Auto, Motorrad, Lkw oder Bus – wir machen dich sicher und selbstbewusst für den Straßenverkehr fit. Mit erfahrenen Fahrlehrern, digitalen Lernmethoden und einem aktuellen Fuhrpark begleiten wir dich persönlich auf deinem Weg zum Führerschein. Zusätzlich bieten wir Auffrischungskurse, Intensivkurse und Berufskraftfahrerschulungen.

```html
<!DOCTYPE html>
<html lang="de">
<head>
<meta charset="utf-8">
<title>Fahrschule Sonnenkamp – Flyer</title>
<link href="https://fonts.googleapis.com/css2?family=Figtree:wght@400;500;600;700;800&display=swap" rel="stylesheet">
<style>
  :root{
    --stage:#cbced6;
    --navy:#252833;
    --teal:#1fb0ad;
    --teal-bright:#18b3b3;
    --white:#ffffff;
    --ink:#1f2129;
    --text-soft:#e9ebef;
  }
  *{margin:0;padding:0;box-sizing:border-box}
  html,body{width:1200px;height:1117px;overflow:hidden;background:var(--stage);font-family:"Figtree",sans-serif}
  .flyer{position:absolute;left:252px;top:66px;width:695px;height:984px;background:var(--navy);overflow:hidden;box-shadow:4px 6px 10px rgba(0,0,0,.18)}
  .hero-photo{position:absolute;right:0;top:0;width:380px;height:345px;
    background:radial-gradient(ellipse at 62% 40%,#b08a6e 0%,#7b6658 28%,#4c4a4e 55%,rgba(37,40,51,0) 80%),
               linear-gradient(90deg,rgba(37,40,51,1) 0%,rgba(60,62,68,.6) 35%,#6d6a68 100%)}
  .brand{position:absolute;left:46px;top:30px;display:flex;align-items:center;gap:12px}
  .brand-mark{width:56px;height:56px;border-radius:50%;background:var(--teal)}
  .brand-name{font-weight:800;font-size:29px;color:var(--white);letter-spacing:.5px;text-transform:uppercase}
  .tagline{position:absolute;left:60px;top:113px;font-size:14px;font-weight:700;color:var(--white);letter-spacing:.3px}
  .headline{position:absolute;left:56px;top:152px;font-size:39px;line-height:39px;font-weight:600;color:var(--teal);letter-spacing:-.3px}
  .intro{position:absolute;left:56px;top:239px;width:370px;font-size:12px;line-height:17.6px;color:var(--text-soft)}
  .bands{position:absolute;left:0;top:340px;width:695px;height:70px}
  .gallery{position:absolute;left:43px;top:309px;display:flex;gap:0}
  .gallery-photo{width:304px;height:140px;border:5px solid var(--white);border-radius:15px;
    background:linear-gradient(180deg,#e6e6e4 0%,#cfd3d6 45%,#b7b2ab 75%,#8f8a84 100%)}
  .section-title{position:absolute;left:0;width:695px;top:466px;text-align:center;font-size:30px;font-weight:600;color:var(--teal)}
  .section-rule{position:absolute;left:56px;top:514px;width:589px;height:2px;background:var(--teal)}
  .timeline{position:absolute;border-left:1.5px dashed var(--teal);height:96px;top:607px}
  .hex{position:absolute;width:54px;height:60px}
  .class{position:absolute;width:222px;color:var(--text-soft)}
  .class h3{font-size:21px;font-weight:600;color:var(--teal);line-height:22px;margin-bottom:4px}
  .class p{font-size:9.4px;line-height:12.6px;letter-spacing:-.15px;margin-bottom:5px}
  .footer-white{position:absolute;left:0;top:908px;width:695px;height:63px;background:var(--white)}
  .footer-strip{position:absolute;left:0;top:971px;width:695px;height:13px;background:var(--teal-bright)}
  .footer-teal{position:absolute;left:0;top:916px;width:360px;height:68px}
  .phone{position:absolute;left:40px;top:924px;display:flex;gap:8px;align-items:flex-start}
  .phone-number{font-size:31px;font-weight:800;color:var(--ink);line-height:30px;letter-spacing:-.3px}
  .email{font-size:14.5px;font-weight:600;color:var(--ink);letter-spacing:.5px;margin-top:1px}
  .address{position:absolute;left:372px;top:928px;display:flex;gap:6px;font-size:16px;line-height:16px;color:var(--ink)}
</style>
</head>
<body>
<article class="flyer">
  <div class="hero-photo" role="img" aria-label="Foto: lächelnder junger Fahrschüler am Steuer eines Autos"></div>

  <div class="brand"><span class="brand-mark"></span><span class="brand-name">Sonnenkamp</span></div>
  <p class="tagline">Mehr als nur eine Fahrschule</p>

  <h1 class="headline">Dein Führerschein -<br>made in Rastede.</h1>
  <p class="intro">Wir sind eine moderne, innovative Fahrschule. Die auf moderne, Ausbildungsfahrzeuge um Ausbildungsmittel setzt. Erfahrene Fahrlehrer moderne Schulungsräume.</p>

  <svg class="bands" viewBox="0 0 695 70" aria-hidden="true">
    <polygon points="0,0 60,8 60,26 0,18" fill="#18b3b3"/>
    <polygon points="0,20 60,28 60,50 0,42" fill="#ffffff"/>
    <polygon points="695,0 635,8 635,26 695,18" fill="#18b3b3"/>
    <polygon points="695,20 635,28 635,50 695,42" fill="#ffffff"/>
  </svg>

  <div class="gallery">
    <div class="gallery-photo" role="img" aria-label="Foto: Schulungsraum mit Stühlen und großem Bildschirm"></div>
    <div class="gallery-photo" role="img" aria-label="Foto: Schulungsraum mit Fahrsimulator und Stühlen"></div>
  </div>

  <h2 class="section-title">Unsere Führerscheinklassen</h2>
  <div class="section-rule"></div>

  <div class="timeline" style="left:88px"></div>
  <div class="timeline" style="left:386px"></div>

  <svg class="hex" style="left:62px;top:536px" viewBox="0 0 54 60" aria-hidden="true">
    <polygon points="27,2 52,16 52,44 27,58 2,44 2,16" fill="#1fb0ad" stroke="#fff" stroke-width="3"/>
    <circle cx="18" cy="35" r="5" fill="none" stroke="#fff" stroke-width="2"/><circle cx="37" cy="35" r="5" fill="none" stroke="#fff" stroke-width="2"/>
    <path d="M18 35 L24 27 L32 27 L37 35 M30 23 L34 23" fill="none" stroke="#fff" stroke-width="2.2" stroke-linecap="round"/>
  </svg>
  <svg class="hex" style="left:62px;top:712px" viewBox="0 0 54 60" aria-hidden="true">
    <polygon points="27,2 52,16 52,44 27,58 2,44 2,16" fill="#1fb0ad" stroke="#fff" stroke-width="3"/>
    <path d="M14 36 V30 L18 23 H36 L40 30 V36 Z" fill="#fff"/>
    <circle cx="20" cy="37" r="3" fill="#1fb0ad"/><circle cx="34" cy="37" r="3" fill="#1fb0ad"/>
    <rect x="20" y="25" width="14" height="5" fill="#1fb0ad"/>
  </svg>
  <svg class="hex" style="left:360px;top:536px" viewBox="0 0 54 60" aria-hidden="true">
    <polygon points="27,2 52,16 52,44 27,58 2,44 2,16" fill="#1fb0ad" stroke="#fff" stroke-width="3"/>
    <path d="M13 22 H31 V37 H13 Z M31 27 H37 L41 32 V37 H31 Z" fill="#fff"/>
    <circle cx="19" cy="38" r="3" fill="#fff" stroke="#1fb0ad" stroke-width="1.5"/><circle cx="36" cy="38" r="3" fill="#fff" stroke="#1fb0ad" stroke-width="1.5"/>
  </svg>
  <svg class="hex" style="left:360px;top:712px" viewBox="0 0 54 60" aria-hidden="true">
    <polygon points="27,2 52,16 52,44 27,58 2,44 2,16" fill="#1fb0ad" stroke="#fff" stroke-width="3"/>
    <rect x="17" y="19" width="20" height="20" rx="3" fill="#fff"/>
    <rect x="20" y="23" width="14" height="7" fill="#1fb0ad"/>
    <circle cx="21" cy="34" r="1.6" fill="#1fb0ad"/><circle cx="33" cy="34" r="1.6" fill="#1fb0ad"/>
    <rect x="19" y="39" width="3" height="3" fill="#fff"/><rect x="32" y="39" width="3" height="3" fill="#fff"/>
  </svg>

  <section class="class" style="left:130px;top:555px">
    <h3>Klasse A</h3>
    <p>Die Führerscheinklasse A berechtigt zum Führen von Krafträdern (Motorrädern) ohne Leistungsbeschränkung.</p>
    <p>Dazu zählen: Alle Motorräder, unabhängig von Hubraum oder Leistung Dreirädrige Kraftfahrzeuge mit mehr als 15 kW Leistung Mindestalter: 24 Jahre (Direkteinstieg) 20 Jahre (nach 2 Jahren Besitz der Klasse A2) 21 Jahre für dreirädrige Fahrzeuge über 15 kW Klasse A umfasst auch die Klassen A2, A1 und AM.</p>
  </section>
  <section class="class" style="left:130px;top:733px">
    <h3>Klasse B</h3>
    <p>Die Führerscheinklasse B berechtigt zum Führen von Pkw und leichte Nutzfahrzeuge bis 3,5 Tonnen zulässiger Gesamtmasse Anhänger bis 750 kg oder schwerer, sofern die Gesamtmasse beider Fahrzeuge 3.500 kg nicht übersteigt Fahrzeuge mit maximal 8 Sitzplätzen zusätzlich zum Fahrersitz.</p>
    <p>Mindestalter: 18 Jahre (bzw. 17 Jahre beim begleiteten Fahren – "BF17")</p>
  </section>
  <section class="class" style="left:429px;top:555px">
    <h3>Klasse C</h3>
    <p>Die Führerscheinklasse C berechtigt zum Führen von: Lkw über 3,5 Tonnen zulässiger Gesamtmasse Zugfahrzeugen mit Anhängern bis 750 kg Keine Personenbeförderung (außer mit zusätzlicher Qualifikation) Mindestalter: 21 Jahre (oder 18 Jahre mit Berufskraftfahrerqualifikation)</p>
    <p>Voraussetzung: Besitz der Klasse B Die Klasse C schließt nicht automatisch die Klasse CE (mit schweren Anhängern) ein.</p>
  </section>
  <section class="class" style="left:429px;top:733px">
    <h3>Klasse D</h3>
    <p>Die Führerscheinklasse D berechtigt zum Führen von: Kraftomnibussen (Busse) mit mehr als 8 Sitzplätzen (ohne Fahrersitz) Mit Anhänger bis 750 kg zulässiger Gesamtmasse Mindestalter: 21 Jahre (bzw. 18 Jahre mit Berufskraftfahrerqualifikation)</p>
    <p>Voraussetzung: Besitz der Klasse B Für den Personenverkehr ist oft zusätzlich eine Weiterbildung (z.B. Personenbeförderungsschein) nötig.</p>
  </section>

  <div class="footer-white"></div>
  <div class="footer-strip"></div>
  <svg class="footer-teal" viewBox="0 0 360 68" aria-hidden="true">
    <polygon points="0,0 330,0 360,68 0,68" fill="#18b3b3"/>
  </svg>

  <div class="phone">
    <svg width="38" height="38" viewBox="0 0 24 24" aria-hidden="true">
      <path d="M6.6 10.8a15 15 0 0 0 6.6 6.6l2.2-2.2a1 1 0 0 1 1-.25 11.4 11.4 0 0 0 3.6.57 1 1 0 0 1 1 1V20a1 1 0 0 1-1 1A17 17 0 0 1 3 4a1 1 0 0 1 1-1h3.5a1 1 0 0 1 1 1c0 1.25.2 2.45.57 3.57a1 1 0 0 1-.25 1z" fill="#1f2129"/>
      <path d="M14.5 3.5a6 6 0 0 1 6 6M14.5 6.5a3 3 0 0 1 3 3" fill="none" stroke="#1f2129" stroke-width="1.6" stroke-linecap="round"/>
    </svg>
    <div>
      <div class="phone-number">0174 5550123</div>
      <div class="email">info@sonnenkamp-fahrschule.de</div>
    </div>
  </div>

  <div class="address">
    <svg width="12" height="17" viewBox="0 0 12 17" aria-hidden="true">
      <path d="M6 0a6 6 0 0 0-6 6c0 4.5 6 11 6 11s6-6.5 6-11a6 6 0 0 0-6-6z" fill="#1fb0ad"/>
      <circle cx="6" cy="6" r="2.3" fill="#fff"/>
    </svg>
    <span>Lindenallee 12,<br>26180 Rastede</span>
  </div>
</article>
</body>
</html>
```